New business card design to go with our new logo

just want an eye-catching business card to go with our new logo. We are open to double sided or single sided. Just want it to have the following info on it. Whatever layout you think looks best.

First and Last Name
Title
Phone 801-555-7392
Address 214 W. Cedar Lane Pleasant Grove UT 84062
Email thecrew@marloweskennelandtreat.example

```html
<!DOCTYPE html>
<html lang="en">
<head>
<meta charset="utf-8">
<title>Marlowe's Kennel &amp; Treat – Business Card</title>
<link rel="stylesheet" href="https://fonts.googleapis.com/css2?family=Marcellus&family=Roboto:wght@400;500&display=swap">
<style>
  :root {
    --backdrop: #2b2b2b;
    --card-white: #f3f3f3;
    --brand-blue: #2fa8d8;
    --brand-orange: #f78c4f;
    --text-grey: #4a4a4a;
    --white: #ffffff;
  }
  * { margin: 0; padding: 0; box-sizing: border-box; }
  html, body {
    width: 1200px;
    height: 960px;
    overflow: hidden;
    background: var(--backdrop);
  }
  .canvas {
    position: relative;
    width: 1200px;
    height: 960px;
  }
  .card {
    position: absolute;
    width: 600px;
    height: 343px;
    overflow: hidden;
  }
  .card--front {
    left: 314px;
    top: 113px;
    background: var(--card-white);
  }
  .card--back {
    left: 311px;
    top: 472px;
    background: var(--brand-blue);
  }

  /* Front */
  .brand-name {
    position: absolute;
    left: 28px;
    top: 30px;
    font-family: "Marcellus", serif;
    font-weight: 400;
    font-size: 31px;
    line-height: 1.12;
    color: var(--brand-orange);
  }
  .brand-name span { display: block; }
  .person {
    position: absolute;
    left: 28px;
    top: 156px;
  }
  .person__name {
    font-family: "Marcellus", serif;
    font-weight: 400;
    font-size: 23px;
    letter-spacing: 0.5px;
    color: var(--brand-blue);
    line-height: 1;
  }
  .person__title {
    margin-top: 5px;
    font-family: "Marcellus", serif;
    font-size: 15px;
    letter-spacing: 0.5px;
    color: var(--brand-orange);
  }
  .contact {
    position: absolute;
    left: 28px;
    top: 209px;
    font-family: "Roboto", sans-serif;
    font-size: 14.5px;
    line-height: 18.5px;
    color: var(--text-grey);
  }
  .contact__address { margin-bottom: 8px; }
  .contact__email { font-size: 13.5px; }
  .illustration {
    position: absolute;
    left: 322px;
    top: 0;
    width: 278px;
    height: 343px;
    background: linear-gradient(112deg, var(--brand-blue) 0%, var(--brand-blue) 58%, var(--brand-orange) 70%, var(--brand-orange) 100%);
  }

  /* Back */
  .back-mark {
    position: absolute;
    left: 232px;
    top: 76px;
    width: 126px;
    height: 126px;
    border: 6px solid var(--white);
    border-radius: 50%;
  }
  .back-brand {
    position: absolute;
    left: 0;
    right: 0;
    top: 208px;
    text-align: center;
    font-family: "Marcellus", serif;
    font-weight: 400;
    font-size: 34px;
    line-height: 1.1;
    color: var(--white);
  }
  .back-brand span { display: block; }
</style>
</head>
<body>
  <main class="canvas">
    <section class="card card--front">
      <div class="brand-name"><span>Marlowe's</span><span>Kennel &amp; Treat</span></div>

      <div class="person">
        <h1 class="person__name">OWEN PARKER</h1>
        <p class="person__title">CEO/FOUNDER</p>
      </div>

      <div class="contact">
        <p class="contact__address">214 W. Cedar Lane<br>Pleasant Grove UT 84062</p>
        <p class="contact__phone">Phone: 801-555-7392</p>
        <p class="contact__email">thecrew@marloweskennelandtreat.example</p>
        <p class="contact__web">www.marloweskennelandtreat.com</p>
      </div>

      <div class="illustration" role="img" aria-label="Illustration of a seated border collie in blue against an orange band"></div>
    </section>

    <section class="card card--back">
      <div class="back-mark"></div>
      <div class="back-brand"><span>Marlowe's</span><span>Kennel &amp; Treat</span></div>
    </section>
  </main>
</body>
</html>
```